Brixel Consulting Limited

we are a company specialising in assisting New Zealand companies to venture into China on strategy, business development, M&A, and Governance.

Industry/Entity Type

Graphic Design

```html
<!DOCTYPE html>
<html lang="en">
<head>
<meta charset="utf-8">
<title>Brixel Consulting Limited – Business Card</title>
<link rel="stylesheet" href="https://fonts.googleapis.com/css2?family=Arvo:wght@700&family=Arimo:wght@400&display=swap">
<style>
  :root {
    --ink-black: #000000;
    --corner-grey: #2b2a28;
    --paint-red: #e32000;
    --paint-deep: #a81800;
    --paper-light: #f4f4f4;
    --paper-edge: #c6c6c6;
    --title-red: #d2232e;
    --title-navy: #1c2454;
    --panel-white: #ffffff;
    --text-dark: #1e1e1e;
    --logo-border: #9a9a9a;
  }
  * { margin: 0; padding: 0; box-sizing: border-box; }
  html, body {
    width: 1200px;
    height: 720px;
    overflow: hidden;
    background: var(--paper-light);
  }
  .card {
    position: relative;
    width: 1200px;
    height: 720px;
    overflow: hidden;
    background: radial-gradient(ellipse 75% 80% at 62% 40%, var(--paper-light) 0%, #e6e6e6 55%, var(--paper-edge) 100%);
  }
  .header-band {
    position: absolute;
    left: 0;
    top: 0;
    width: 1200px;
    height: 211px;
  }
  .paint-area {
    position: absolute;
    left: 0;
    top: 0;
    width: 553px;
    height: 198px;
    background: linear-gradient(180deg, var(--paint-red) 0%, var(--paint-red) 35%, var(--paint-deep) 100%);
  }
  .logo-box {
    position: absolute;
    left: 736px;
    top: 64px;
    width: 361px;
    height: 126px;
    background: linear-gradient(180deg, #ffffff 0%, #f1f1f1 100%);
    border: 2px dotted var(--logo-border);
    display: flex;
    align-items: center;
    padding-left: 100px;
  }
  .logo-name {
    font-family: "Arimo", Arial, sans-serif;
    font-weight: 400;
    font-size: 26px;
    line-height: 1.2;
    color: var(--ink-black);
    text-align: left;
  }
  .identity {
    position: absolute;
    left: 0;
    width: 1200px;
    text-align: center;
    font-family: "Arvo", "Rockwell", serif;
    font-weight: 700;
    color: var(--title-red);
    -webkit-text-stroke: 2px var(--title-navy);
    paint-order: stroke fill;
    white-space: nowrap;
  }
  .person-name {
    top: 316px;
    font-size: 64px;
    line-height: 1;
    letter-spacing: 3px;
  }
  .person-role {
    top: 410px;
    font-size: 44px;
    line-height: 1;
    letter-spacing: 3px;
  }
  .contact-panel {
    position: absolute;
    left: 35px;
    top: 485px;
    width: 1073px;
    height: 171px;
    background: var(--panel-white);
    padding-top: 17px;
  }
  .contact-line {
    font-family: "Arimo", Arial, sans-serif;
    font-size: 28px;
    line-height: 35px;
    color: var(--text-dark);
    letter-spacing: 1px;
    white-space: nowrap;
  }
  .contact-line.phone, .contact-line.skype { padding-left: 3px; }
  .contact-line.email { margin-left: -2px; }
</style>
</head>
<body>
<main class="card">
  <svg class="header-band" viewBox="0 0 1200 211" preserveAspectRatio="none" aria-hidden="true">
    <rect x="0" y="0" width="1200" height="211" fill="var(--corner-grey)"/>
    <path d="M0,0 H1077 C1136,2 1179,43 1200,91 V211 H0 Z" fill="var(--ink-black)"/>
  </svg>

  <div class="paint-area" role="img" aria-label="Red paint dripping down over the black header band"></div>

  <div class="logo-box">
    <p class="logo-name">Brixel<br>Consulting<br>Limited</p>
  </div>

  <h1 class="identity person-name">MARA-LIN HOVE</h1>
  <h2 class="identity person-role">MANAGING DIRECTOR</h2>

  <section class="contact-panel">
    <p class="contact-line phone">Phone: +64 21 555 0147</p>
    <p class="contact-line skype">Skype:maralinhoveconsulting</p>
    <p class="contact-line email">email address: mara-lin.hove@brixelconsulting.com</p>
  </section>
</main>
</body>
</html>
```